Drug Side Effects

We need 3 custom illustrations done for our website PillPerilNote.com.

We will be adding these illustrations to these pages:
http://www.pillperilnote.com/testosterone/lawsuit.htm

We will be using statistics and ideas from an infographic already created (see attached). Please make these look completely different and use our color scheme to match them up

#3 From Infographic 1
Please use all of the information from #3 except the middle paragraph.

#2 Alleged Side Effects from Infographic 2
Please use all of the information from this section, do not use any weird fonts, do not mention "increased risk of prostate cancer"

#3 Products that increase testosterone from Infographic 2
Please copy this exactly, use different pill bottle

These should all fit the width of our site and be able to be easily integrated.
Updates

Target Market(s)

We are targeting people who are searching for testosterone related therapies, so this is older males between the ages of 40-80

Industry/Entity Type

Drug

Font styles to use
Serif
Sans Serif

Colors
34a6d7
3176b5
33b7a4
86cfc6
33a6d7

Requirements
Must have
• Must look professional like something you would find in a medical journal or CuraLog
Should not have
• cartoonish images

```html
<!DOCTYPE html>
<html lang="en">
<head>
<meta charset="utf-8">
<title>How Many American Men Are Undergoing Testosterone Therapy?</title>
<link rel="stylesheet" href="https://fonts.googleapis.com/css2?family=Arimo:wght@400;700&family=Oswald:wght@500&display=swap">
<style>
  :root {
    --banner-blue: #2f77b7;
    --deep-blue: #3176b5;
    --teal: #33b7a4;
    --white: #ffffff;
    --page: #ffffff;
  }
  html, body {
    margin: 0;
    padding: 0;
    width: 1200px;
    height: 965px;
    overflow: hidden;
    background: var(--page);
  }
  .stat-card {
    position: relative;
    width: 650px;
    height: 522.7px;
    transform: scale(1.84615);
    transform-origin: 0 0;
    font-family: "Arimo", Arial, sans-serif;
  }
  .banner {
    position: absolute;
    left: 0;
    top: 0;
    width: 640px;
    height: 186px;
  }
  .banner-shape {
    position: absolute;
    inset: 0;
  }
  .banner-title {
    position: absolute;
    left: 0;
    top: 68px;
    width: 640px;
    margin: 0;
    text-align: center;
    color: var(--white);
    font-weight: 400;
    font-size: 26.5px;
    line-height: 38px;
  }
  .banner-title .highlight {
    color: var(--teal);
    font-weight: 700;
  }
  .stat-figure {
    position: absolute;
    left: 18px;
    top: 196px;
    margin: 0;
    font-family: "Oswald", "Arial Narrow", sans-serif;
    font-weight: 500;
    font-size: 182px;
    line-height: 1;
    letter-spacing: 1px;
    color: var(--teal);
    white-space: nowrap;
    transform: scaleX(0.8);
    transform-origin: 0 0;
  }
  .stat-caption {
    position: absolute;
    left: 22px;
    top: 392px;
    width: 314px;
    margin: 0;
    color: var(--teal);
    font-size: 25.5px;
    line-height: 31.5px;
    white-space: nowrap;
  }
  .stat-caption .line {
    display: block;
  }
  .stat-caption .line.spread {
    text-align: justify;
    text-align-last: justify;
  }
  .method-icons {
    position: absolute;
    inset: 0;
  }
  .method-label {
    position: absolute;
    margin: 0;
    color: var(--teal);
    font-weight: 700;
    line-height: 1;
  }
  .label-iv { left: 554px; top: 252px; font-size: 38px; }
  .label-oral { left: 533px; top: 443px; font-size: 27px; }
  .label-patch { left: 369px; top: 494px; font-size: 27px; }
</style>
</head>
<body>
  <main class="stat-card">
    <header class="banner">
      <svg class="banner-shape" viewBox="0 0 640 186" aria-hidden="true">
        <polygon points="20,36 55,4 90,36" fill="var(--banner-blue)"/>
        <rect x="0" y="35" width="640" height="151" fill="var(--banner-blue)"/>
      </svg>
      <h1 class="banner-title">How Many American Men Are<br>Undergoing Testosterone <span class="highlight">THERAPY</span>?</h1>
    </header>

    <p class="stat-figure">2.9%</p>
    <p class="stat-caption">
      <span class="line spread">Of American men, age</span>
      <span class="line spread">40 or older are under-</span>
      <span class="line spread">going testosterone</span>
      <span class="line">thearpy.</span>
    </p>

    <svg class="method-icons" viewBox="0 0 650 523" aria-hidden="true">
      <rect x="455" y="213" width="76" height="118" rx="14" fill="var(--deep-blue)"/>
      <circle cx="493" cy="225" r="4" fill="var(--white)"/>
      <rect x="466" y="240" width="54" height="74" rx="6" fill="var(--teal)"/>
      <rect x="485" y="330" width="16" height="16" fill="var(--deep-blue)"/>
      <path d="M493 346 V352 C493 395 540 392 548 350 C553 322 560 312 575 312" fill="none" stroke="var(--deep-blue)" stroke-width="3"/>
      <rect x="573" y="305" width="28" height="12" rx="5" fill="var(--deep-blue)"/>
      <rect x="585" y="308" width="8" height="6" fill="var(--teal)"/>
      <line x1="600" y1="311" x2="612" y2="311" stroke="var(--teal)" stroke-width="2"/>
      <rect x="369" y="384" width="101" height="95" rx="12" fill="var(--deep-blue)"/>
      <rect x="391" y="404" width="57" height="55" fill="var(--teal)"/>
      <path d="M533 475 H576 V512 H533 A18.5 18.5 0 0 1 533 475 Z" fill="var(--teal)"/>
      <path d="M576 475 H621 A18.5 18.5 0 0 1 621 512 H576 Z" fill="var(--deep-blue)"/>
    </svg>

    <p class="method-label label-iv">IV</p>
    <p class="method-label label-oral">ORAL</p>
    <p class="method-label label-patch">PATCH</p>
  </main>
</body>
</html>
```